Help Give House Painter “Fresh” Website Makeover!

A residential and commercial painting company based in Albuquerque, NM, USA needs a fresh, new, fun, and playful--yet, simple, elegant and professional--website made.

Here is a link to their existing site:

http://brelkocoatings.example/

We want to keep a similar site structure., So the navigation layout will stay the same. However, the video is too small, is too far over in the sidebar, and the overall design is amateur at best. We want something bright, colorful and bold!

We will need a space for the Video above the fold, and there needs to be space in the design for Testimonials, Specials and Images. It’s also very important to have the Morvel Roster awards that you see on his current website.

Please also include somewhere in the Design icons for ClipNest, FriendLoop, Zentri+ and WorkLattice.

Here are some examples to look at to get your creative juices flowing!

http://quillbarrowcoats.example/

http://www.tvnb.example/

http://www.dunmore-ashby.example/

http://www.nookpages.example/painting-company-nook-page/

http://www.virtudeskworks.example/website-templates/painting-company-website-template-81937.html

We have accounts at both pixcrate.example and snaplode.example. If you use placeholder images from there, that's fine. We can buy the images when and if your design is selected.

Target Market(s)

The audience is the average middle class homeowner to higher upper class. This should appeal to families, couples, and singles who own a home.

Industry/Entity Type

Residential

Font styles to use
Sans Serif

Requirements
Must have
• - - Lots of color! It's a site about painting homes. People like a variety of colors. Bring out your inner artist, and get bold with your colors!

- - A video place holder. As you can see, there is a video on the existing site, but it's small and hidden. Make it big and put it top left, or in the center.

- -Detailed and organized PSD structure. We're going to turn your design into a website, and to make that work soothly, we ask that you organize you PSD well: name your layers, keep things separated, group and ungroup as necessary, etc.

- A sidebar that goes down the right side of an interior page. We need a homepage, and also one [1] interior page template. We don't need you to make a design for each page. Just the homepage, followed by a simple interior page design that requires only the header/navigation, and a sidebar down the right side.
Should not have
• - Coding. This is a design project only.

```html
<!DOCTYPE html>
<html lang="en">
<head>
<meta charset="utf-8">
<title>Brelko's Painting — Not Just Another Painter</title>
<link href="https://fonts.googleapis.com/css2?family=Oswald:wght@400;500;700&family=Open+Sans:wght@400;600;700&display=swap" rel="stylesheet">
<style>
:root{
  --blue:#0f5fb3;
  --navy:#0d2a6b;
  --red:#e51c23;
  --orange:#f8ad2f;
  --orange-dark:#f39a12;
  --gold:#d9b43a;
  --text:#444;
  --dark:#1c1c1c;
  --footer:#0e0e0e;
  --footer-col:#2b2b2b;
  --card-bg:#ececec;
  --white:#fff;
}
*{box-sizing:border-box;margin:0;padding:0}
html,body{width:885px;height:1200px;overflow:hidden;background:var(--white)}
body{font-family:"Open Sans",Arial,sans-serif;color:var(--text)}
.page{position:relative;width:897px;height:1216px;transform:scale(.9866);transform-origin:0 0}
.abs{position:absolute}
.line{display:block;white-space:nowrap}

/* header */
.header{left:0;top:0;width:897px;height:110px;background:var(--white);border-top:3px dotted var(--red)}
.brand-mark{left:100px;top:14px;width:72px;height:72px;border-radius:50%;background:var(--blue)}
.brand-name{left:190px;top:20px;font-family:"Oswald",sans-serif;font-weight:700;font-size:27px;color:var(--blue);letter-spacing:-.3px}
.brand-tagline{left:190px;top:63px;font-weight:700;font-size:13px;color:var(--dark)}
.award{width:50px;height:66px;top:14px;background:var(--gold);border-radius:6px 6px 25px 25px}
.award-caption{top:86px;font-weight:700;font-size:12px;color:var(--dark)}
.contact-phone{right:102px;top:15px;font-size:14px;color:var(--blue);font-weight:600}
.contact-mail{right:100px;top:39px;font-size:12px;color:var(--blue);font-weight:600;display:flex;align-items:center;gap:6px}
.social{display:flex;gap:9px}
.social-dot{width:27px;height:27px;border-radius:50%;border:3px solid #2e8c9e;background:var(--gold)}
.social-dot.red{background:#c9252c}
.sr{position:absolute;width:1px;height:1px;overflow:hidden;clip:rect(0 0 0 0)}

/* nav */
.nav{left:0;top:110px;width:897px;height:42px;background:linear-gradient(#fbc65a,var(--orange) 60%,var(--orange-dark))}
.nav ul{list-style:none;display:flex;position:absolute;left:98px;top:0;height:42px}
.nav li{font-family:Arial,sans-serif;font-weight:700;font-size:11px;color:var(--dark);padding:0 9px;line-height:42px;border-right:1px solid rgba(0,0,0,.08)}
.nav li.current{background:var(--blue);color:var(--white);padding:0 14px}

/* hero */
.hero{left:0;top:152px;width:897px;height:328px;background:linear-gradient(90deg,#f05a22 0%,#ee5320 45%,#f4c9b0 62%,#f0e6df 100%)}
.video{left:98px;top:190px;width:352px;height:279px;border-radius:6px;overflow:hidden;background:#222;box-shadow:0 2px 8px rgba(0,0,0,.35)}
.video-frame{position:absolute;left:0;top:0;width:352px;height:255px;background:linear-gradient(135deg,#b8d77a,#9cc46a 40%,#e0a27c 70%,#d9d9d9)}
.video-play{position:absolute;left:170px;top:113px;width:28px;height:28px;border-radius:50%;background:var(--white);opacity:.95}
.video-play:after{content:"";position:absolute;left:11px;top:8px;border-left:9px solid #333;border-top:6px solid transparent;border-bottom:6px solid transparent}
.video-bar{position:absolute;left:0;top:255px;width:352px;height:24px;background:#111;color:var(--white);font-size:8px;font-weight:700}
.video-bar .t1{position:absolute;left:32px;top:7px}
.video-bar .t2{position:absolute;left:268px;top:7px}
.video-track{position:absolute;left:60px;top:10px;width:188px;height:4px;border-radius:2px;background:#3a3a3a}
.video-track i{display:block;width:62px;height:4px;border-radius:2px;background:#6a6a6a}

.estimate{left:532px;top:204px;width:248px;height:276px;background:rgba(60,60,60,.82)}
.estimate h2{height:35px;background:var(--blue);color:var(--white);font-family:"Oswald",sans-serif;font-weight:500;font-size:17px;padding:6px 0 0 19px;letter-spacing:.2px}
.field{position:absolute;left:18px;width:209px;height:22px;background:var(--white);border-radius:2px;font-size:9px;font-weight:600;color:#555;padding:4px 7px}
.captcha-label{position:absolute;left:19px;top:196px;color:var(--white);font-size:9px;font-weight:700}
.captcha{position:absolute;left:160px;top:193px;width:66px;height:17px;background:var(--red);color:var(--white);font-size:8px;font-weight:700;font-style:italic;letter-spacing:5px;text-align:center;line-height:17px}
.btn-continue{position:absolute;left:17px;top:246px;width:72px;height:25px;background:var(--blue);color:var(--white);font-size:11px;font-weight:700;text-align:center;line-height:25px;border-radius:2px}

/* welcome */
.welcome{left:98px;top:500px;width:698px}
.welcome h1{font-family:"Oswald",sans-serif;font-weight:400;font-size:18px;color:var(--dark);padding-bottom:6px;border-bottom:1px solid #ddd;position:relative}
.welcome h1 span{color:var(--red)}
.welcome h1:after{content:"";position:absolute;left:0;bottom:-2px;width:80px;height:3px;background:var(--red)}
.welcome p{font-size:10.1px;line-height:17px;margin-top:13px}
.welcome p + p{margin-top:8px}
.btn-read{display:inline-block;margin-top:13px;background:var(--blue);color:var(--white);font-size:10.5px;font-weight:700;padding:0 9px;line-height:24px;border-radius:3px;box-shadow:0 2px 0 #0a4382}

/* feature cards */
.card{top:711px;width:216px;height:258px;background:var(--card-bg);border-radius:5px;box-shadow:0 8px 10px -6px rgba(0,0,0,.25);overflow:hidden}
.card h3{height:56px;font-family:"Oswald",sans-serif;font-weight:400;font-size:17px;line-height:23px;color:var(--white);padding:4px 0 0 16px;text-transform:uppercase}
.card .shot{position:absolute;left:12px;top:68px;width:193px;height:83px;border:3px solid}
.card p{position:absolute;left:12px;top:160px;width:195px;font-size:10.1px;line-height:13.6px;color:#333}
.card .more{position:absolute;left:12px;top:232px;font-size:9px;font-weight:700;color:#222}
.card-navy h3{background:var(--navy)}.card-navy .shot{border-color:var(--navy);background:linear-gradient(135deg,#9ed04f,#7ab84a 50%,#d8c9a9)}
.card-red h3{background:var(--red)}.card-red .shot{border-color:var(--red);background:linear-gradient(135deg,#5aaedc,#8fcbe8 50%,#c9e3ef)}
.card-orange h3{background:var(--orange)}.card-orange .shot{border-color:var(--orange);background:linear-gradient(135deg,#a7d25f,#e9a77f 55%,#dfe7cf)}

/* footer */
.footer{left:0;top:1008px;width:897px;height:208px;background:var(--footer);color:var(--white)}
.testimonials{left:99px;top:0;width:216px;height:208px;background:var(--footer-col)}
.testimonials h4{position:absolute;left:46px;top:15px;font-family:"Oswald",sans-serif;font-weight:400;font-size:17px}
.quote{position:absolute;left:8px;top:50px;width:198px;height:117px;background:var(--white);border-radius:5px;color:#222;font-size:9px;font-style:italic;line-height:16.6px;padding:6px 6px 0 12px}
.quote .first{padding-left:16px}
.quote:before{content:"\201C";position:absolute;left:8px;top:-2px;font-size:28px;color:#bbb;font-style:normal;font-family:Georgia,serif}
.quote-tail{position:absolute;left:30px;top:166px;border-top:12px solid var(--white);border-right:14px solid transparent}
.avatar{position:absolute;left:145px;top:145px;width:52px;height:52px;border-radius:50%;background:linear-gradient(#d7d2cc,#9c948c);border:2px solid var(--white)}
.quote-name{position:absolute;left:22px;top:183px;font-weight:700;font-size:11.5px}
.news-title{left:342px;top:15px;font-family:"Oswald",sans-serif;font-weight:400;font-size:14px}
.news-input{left:341px;top:42px;width:212px;height:27px;background:var(--white);color:#8a8a4a;font-size:8.5px;padding:8px}
.news-submit{left:559px;top:42px;width:64px;height:27px;background:var(--navy);font-size:11.5px;text-align:center;line-height:27px}
.rule-v{width:1px;background:#333}
.rule-h{height:1px;background:#333}
.footer-address{left:362px;top:105px;width:120px;font-size:9.5px;line-height:16px}
.footer-phone{right:266px;top:106px;font-size:11px;display:flex;align-items:center;gap:9px}
.footer-mail{right:266px;top:132px;font-size:10px;display:flex;align-items:center;gap:7px;white-space:nowrap}
.follow-title{left:678px;top:15px;font-family:"Oswald",sans-serif;font-weight:400;font-size:14px}
.partners{left:657px;top:100px;width:140px;height:53px;background:var(--white);border-radius:3px}
.partner-a{position:absolute;left:5px;top:7px;width:68px;height:38px;background:#1b5ea6;border-radius:2px}
.partner-b{position:absolute;left:77px;top:0;width:63px;height:53px;background:var(--navy);border-radius:0 3px 3px 0}
.copyright{right:101px;top:184px;font-size:10.5px;font-weight:700}
</style>
</head>
<body>
<div class="page">

  <header class="header abs">
    <div class="brand-mark abs" role="img" aria-label="Brelko's Painting brand mark"></div>
    <div class="brand-name abs">Brelko's Painting</div>
    <div class="brand-tagline abs">Not Just Another Painter</div>

    <div class="award abs" style="left:420px" role="img" aria-label="Morvel Roster service award badge"></div>
    <div class="award-caption abs" style="left:392px">Exterior Painting</div>
    <div class="award abs" style="left:535px" role="img" aria-label="Morvel Roster service award badge"></div>
    <div class="award-caption abs" style="left:511px">Interior Painting</div>

    <div class="contact-phone abs">
      <svg width="9" height="12" viewBox="0 0 9 12" style="vertical-align:-1px"><path d="M2 0h2l1 3-1.5 1c.6 1.6 1.4 2.8 2.7 3.8L7.5 6.6 9 8.5 7.7 10.4C4 10 .5 5.5 1 .8z" fill="#0f5fb3"/></svg>
      505-555-0142
    </div>
    <div class="contact-mail abs">
      <svg width="14" height="10" viewBox="0 0 14 10"><rect x=".5" y=".5" width="13" height="9" fill="none" stroke="#0f5fb3"/><path d="M.5 .5 7 6l6.5-5.5" fill="none" stroke="#0f5fb3"/></svg>
      info@brelkocoatings.example
    </div>
    <div class="social abs" style="left:668px;top:66px">
      <span class="social-dot" role="img" aria-label="FriendLoop"><span class="sr">FriendLoop</span></span>
      <span class="social-dot" role="img" aria-label="WorkLattice"><span class="sr">WorkLattice</span></span>
      <span class="social-dot red" role="img" aria-label="ClipNest"><span class="sr">ClipNest</span></span>
      <span class="social-dot" role="img" aria-label="Zentri+"><span class="sr">Zentri+</span></span>
    </div>
  </header>

  <nav class="nav abs">
    <ul>
      <li class="current">HOME</li>
      <li>About Us</li>
      <li>Residential Painting</li>
      <li>Commercial Painting</li>
      <li>Specials</li>
      <li>Blog</li>
      <li>Testimonials</li>
      <li>Contact Us</li>
    </ul>
  </nav>

  <section class="hero abs" role="img" aria-label="Orange paint roller stroke with a smiling couple behind the estimate form"></section>

  <div class="video abs">
    <div class="video-frame" role="img" aria-label="Video still of a couple holding paint rollers"></div>
    <div class="video-play"></div>
    <div class="video-bar">
      <svg class="abs" style="left:10px;top:7px" width="9" height="10" viewBox="0 0 9 10"><path d="M0 0l9 5-9 5z" fill="#fff"/></svg>
      <span class="t1">04:59</span>
      <div class="video-track"><i></i></div>
      <span class="t2">10:35</span>
      <svg class="abs" style="left:307px;top:6px" width="12" height="12" viewBox="0 0 12 12"><path d="M0 4h3l4-3v10L3 8H0z" fill="#fff"/><path d="M9 3.5c1.2 1.3 1.2 3.7 0 5" stroke="#fff" fill="none"/></svg>
      <svg class="abs" style="left:326px;top:6px" width="12" height="12" viewBox="0 0 12 12"><path d="M1 1l10 10M1 1h4M1 1v4M11 11H7M11 11V7" stroke="#fff" stroke-width="1.6" fill="none"/></svg>
    </div>
  </div>

  <form class="estimate abs">
    <h2>SCHEDULE FREE ESTIMATE</h2>
    <div class="field" style="top:45px">Your Name</div>
    <div class="field" style="top:78px">Phone Number</div>
    <div class="field" style="top:108px">Email</div>
    <div class="field" style="top:138px;height:46px">Describe What Needs To Be Done</div>
    <div class="captcha-label">Please type the Following:</div>
    <div class="captcha">EBTL</div>
    <div class="field" style="top:219px"></div>
    <div class="btn-continue">Continue</div>
  </form>

  <section class="welcome abs">
    <h1>Welcome To <span>Brelko's Paintings</span></h1>
    <p>
      <span class="line">Lorem ipsum dolor sit amet, consectetuer adipiscing elit, sed diam nonummy nibh euism od tincidunt ut laoreet dolore magna aliquam erat</span>
      <span class="line">volutpat. Ut wisi enim ad minim venia m, quis nostrud exerci in amet ullamcorper suscipit lobortis nisl ut aliquip ex ea comsed diam nonummy</span>
      <span class="line">nibh euism od tincidunt uopre laoreet dolore magna aliquam erat volutpat.</span>
    </p>
    <p>
      <span class="line">Lorem ipsum dolor sit amet, consectetuer adipiscing elit, sed diam nonummy nibh euism od tincidunt ut in laoreet dolore magna aliquam erat volutpat.</span>
      <span class="line">Ut wisi enim ad minim venia m, quis nostrud exerci tationperq ullamcorper suscipit lobortis nisl ut..</span>
      <span class="line">in laoreet dolore magna aliquam erat volutpat. Ut wisi enim ad minim venia m, quis nostrud exerci tationperq ullamcorper suscipit lobortis nisl ut..</span>
    </p>
    <span class="btn-read">Read More</span>
  </section>

  <article class="card card-navy abs" style="left:99px">
    <h3>Our Painting<br>in Albuquerque</h3>
    <div class="shot" role="img" aria-label="Couple painting a wall green"></div>
    <p>Lorem ipsum dolor sit ametuer adipiscingi elit, sed diam nmy nibh euismod tincidunt ut laoreet dolore magna am erat visi enim ad minim veniam, quis nostrud exerci</p>
    <span class="more">READ MORE »</span>
  </article>
  <article class="card card-red abs" style="left:341px">
    <h3>Albuquerque<br>Painter Videos</h3>
    <div class="shot" role="img" aria-label="Painter on a ladder with a blue wall"></div>
    <p>Lorem ipsum dolor sit ametuer adipiscingi elit, sed diam nmy nibh euismod tincidunt ut laoreet dolore magna am erat visi enim ad minim veniam, quis nostrud exerci</p>
    <span class="more">READ MORE »</span>
  </article>
  <article class="card card-orange abs" style="left:583px">
    <h3>Happy Albuquerque<br>Painting Customers</h3>
    <div class="shot" role="img" aria-label="Happy customers holding paint rollers"></div>
    <p>Lorem ipsum dolor sit ametuer adipiscingi elit, sed diam nmy nibh euismod tincidunt ut laoreet dolore magna am erat visi enim ad minim veniam, quis nostrud exerci</p>
    <span class="more">READ MORE »</span>
  </article>

  <footer class="footer abs">
    <div class="testimonials abs">
      <svg class="abs" style="left:10px;top:12px" width="28" height="24" viewBox="0 0 28 24"><rect x="1.5" y="5.5" width="18" height="17" rx="2" fill="none" stroke="#fff" stroke-width="2"/><path d="M10 15l12-12 3 3-12 12-4 1z" fill="#fff"/></svg>
      <h4>Client Testimonials</h4>
      <div class="quote">
        <span class="line first">Lorem ipsum dolor sit amet</span>
        <span class="line">consctueropf adipiscing elit, sed diam</span>
        <span class="line">nonumy nibh euismodg tincidunt ut laoreet</span>
        <span class="line">dolore magna aliquam eratg volutpat. ut</span>
        <span class="line">wisi enim ad minim veniam, quis nostrud</span>
        <span class="line">exerci tation</span>
      </div>
      <div class="quote-tail"></div>
      <div class="avatar" role="img" aria-label="Client portrait"></div>
      <div class="quote-name">Mrs.&nbsp; dapibus eget,</div>
    </div>

    <div class="news-title abs">Sign up for Newsletter</div>
    <div class="news-input abs">Enter Your Email</div>
    <div class="news-submit abs">SUBMIT</div>

    <div class="rule-v abs" style="left:645px;top:30px;height:45px"></div>
    <div class="rule-h abs" style="left:340px;top:88px;width:458px"></div>
    <div class="rule-v abs" style="left:645px;top:100px;height:55px"></div>
    <div class="rule-h abs" style="left:340px;top:168px;width:458px"></div>

    <svg class="abs" style="left:342px;top:108px" width="10" height="14" viewBox="0 0 10 14"><path d="M5 0a5 5 0 0 1 5 5c0 3.5-5 9-5 9S0 8.5 0 5a5 5 0 0 1 5-5z" fill="#fff"/><circle cx="5" cy="5" r="2" fill="#0e0e0e"/></svg>
    <div class="footer-address abs">Lorem ipsum dolor sit amet, consectetuer adipiscing elit,</div>
    <div class="footer-phone abs">
      <svg width="9" height="13" viewBox="0 0 9 13"><rect x=".5" y=".5" width="8" height="12" rx="1.5" fill="#fff"/><rect x="2" y="2" width="5" height="7" fill="#0e0e0e"/></svg>
      505-555-0187
    </div>
    <div class="footer-mail abs">
      <svg width="12" height="9" viewBox="0 0 12 9"><rect width="12" height="9" fill="#fff"/><path d="M0 0l6 5 6-5" fill="none" stroke="#0e0e0e"/></svg>
      info@brelkocoatings.example
    </div>

    <div class="follow-title abs">Follow Us On</div>
    <div class="social abs" style="left:673px;top:42px">
      <span class="social-dot" role="img" aria-label="FriendLoop"><span class="sr">FriendLoop</span></span>
      <span class="social-dot" role="img" aria-label="WorkLattice"><span class="sr">WorkLattice</span></span>
      <span class="social-dot red" role="img" aria-label="ClipNest"><span class="sr">ClipNest</span></span>
      <span class="social-dot" role="img" aria-label="Zentri+"><span class="sr">Zentri+</span></span>
    </div>

    <div class="partners abs">
      <div class="partner-a" role="img" aria-label="Accredited business badge"></div>
      <div class="partner-b" role="img" aria-label="Chamber of commerce badge"></div>
    </div>

    <div class="copyright abs">© 2014 BRELKO'S PAINTING &nbsp;|&nbsp; All Rights Reserved</div>
  </footer>

</div>
</body>
</html>
```